Energy cost saving website (job description rewritten!)

Job Type: WordPress design
Task Outline: Create a WordPress design
Task Description:
We are new business (Germany) in the market of saving costs by power-saving (name: 'uns-gefaellt-der-Ruhetag.de'). This is reached by changing the supplier, the use of LED bulbs, energy saving washing machines, stoves, microwaves, hairdryers, vacuum cleaners and the like - where all of these be selled or affiliated through the website maybe you will create for us.
Design parameters:
We want a serious design that embodies a feeling of honesty, competence and capability.
Visitors should particularly see that this site saves them money!
The home page mainly should act as a selector of possibilities saving money by power-saving, usage of LED bulbs and large energy saving household devices (washing machines, etc.)
Updates
Hello designers,
browsing through the PixelHarbors files of portfolios I found one header graphics which excites me. Please find it here: http://www.pixelharbor-example.com/design/482613/wordpress-design-by-tarun-mehlvi . Note: it is NOT the picture but the shadowing. So if you consider this in your concepts would be another 'nice-to-have'.
Thanks.
Reason: Give more time for newly invited disigners to submit designs.
Reason: Some designs still unter contruction.
Target Market(s)
People looking out for saving money by power-saving.
Industry/Entity Type
Business
Requirements
Must have
- Look and feel of 'this site saves me money'!
Nice to have
- We love 3D effects, but its not a must have. We also like cartoons, but feel free to develop your own concept, please. An appropriate backgrond picture would be nice.
Should not have
- Some kind of these exaggerated smiling or handshaking photos. That bathetic symbols like money bills or coins stacks.

```html
<!DOCTYPE html>
<html lang="de">
<head>
<meta charset="utf-8">
<title>uns-gefaellt-der-Ruhetag.de</title>
<link href="https://fonts.googleapis.com/css2?family=Cabin:wght@400;500;600;700&family=Arimo:wght@400&display=swap" rel="stylesheet">
<style>
:root{
  --orange:#ff6a00;
  --orange-light:#ff9a00;
  --orange-btn:#ff7a10;
  --panel:#e6e7e8;
  --page:#e6e7e8;
  --text:#2b2b2b;
  --white:#ffffff;
}
*{margin:0;padding:0;box-sizing:border-box}
html,body{width:930px;height:1200px;overflow:hidden;background:var(--page)}
body{position:relative;font-family:"Arimo",Arial,sans-serif;color:var(--text)}
.masthead{position:absolute;left:0;top:0;width:930px;height:462px;
  background:linear-gradient(180deg,var(--orange) 0%,var(--orange-light) 18%,var(--orange) 45%,#ff9800 75%,var(--orange) 100%)}
.site-name{position:absolute;left:60px;top:24px;font-family:"Cabin",sans-serif;font-weight:600;font-size:28px;color:var(--white);letter-spacing:-.2px}
.hero{position:absolute;left:59px;top:66px;width:812px;height:345px;background:var(--panel);border:2px solid #f4f4f4;border-radius:3px}
.hero-shadow{position:absolute;left:84px;top:408px;width:760px;height:26px;border-radius:50%;
  background:radial-gradient(ellipse at 50% 20%,rgba(0,0,0,.75) 0%,rgba(0,0,0,.35) 45%,rgba(0,0,0,0) 72%)}
.hero-photo{position:absolute;left:40px;top:33px;width:434px;height:263px;
  background:radial-gradient(ellipse at 50% 50%,#ffffff 0%,#eef0f0 45%,#e6e7e8 100%)}
.hero-copy{position:absolute;left:497px;top:84px;width:300px}
.hero-title{font-family:"Cabin",sans-serif;font-weight:600;font-size:23px;line-height:27px;color:var(--orange);text-transform:uppercase}
.hero-lead{margin-top:8px;width:265px;font-family:"Cabin",sans-serif;font-size:19.5px;line-height:25px;color:#333}
.btn{position:absolute;display:flex;align-items:center;justify-content:center;color:var(--white);font-family:"Cabin",sans-serif;
  background:linear-gradient(180deg,#ff9a3a 0%,var(--orange-btn) 50%,#ff6a00 100%);border:1px solid #ff5a00;border-radius:4px;
  box-shadow:inset 0 1px 0 rgba(255,255,255,.35)}
.btn-learn{left:495px;top:226px;width:116px;height:37px;font-size:17px}
.feature{position:absolute;top:501px;width:245px}
.feature-photo{position:relative;width:237px;height:152px;border:2px solid #f6f6f6;border-radius:3px}
.feature-photo::after{content:"";position:absolute;left:4px;right:4px;bottom:-10px;height:10px;border-radius:50%;
  background:radial-gradient(ellipse at 50% 0%,rgba(0,0,0,.8) 0%,rgba(0,0,0,0) 70%)}
.photo-laundry{background:linear-gradient(135deg,#e9e9e9 0%,#c9b9a4 40%,#6fb8c4 70%,#2c4a7a 100%)}
.photo-meters{background:linear-gradient(180deg,#aee1f5 0%,#9fd6ef 100%)}
.photo-bulbs{background:radial-gradient(ellipse at 50% 55%,#fbfbfb 0%,#e8e9ea 70%,#e2e3e4 100%)}
.feature-text{margin-top:28px;font-size:10.5px;line-height:17.6px;text-align:justify;color:#2e2e2e}
.feature-text p+p{margin-top:17.6px}
.btn-cta{top:1012px;height:37px;font-size:20px;font-weight:700;text-transform:uppercase}
.footer{position:absolute;left:0;top:1117px;width:930px;height:83px;
  background:linear-gradient(180deg,var(--orange-light) 0%,var(--orange) 55%,#ff7a00 100%)}
.footer-nav{position:absolute;left:61px;top:34px;font-size:10px;color:var(--white)}
.footer-nav a{color:var(--white);text-decoration:none}
.footer-nav .sep{margin:0 5px}
.footer-brand{position:absolute;left:631px;top:19px;font-family:"Cabin",sans-serif;font-weight:600;font-size:17px;color:var(--white)}
.footer-copy{position:absolute;left:633px;top:45px;font-size:10px;color:var(--white)}
</style>
</head>
<body>
<header class="masthead">
  <div class="site-name">uns-gefaellt-der-Ruhetag.de</div>
  <div class="hero-shadow"></div>
  <section class="hero">
    <div class="hero-photo" role="img" aria-label="Photo of an LED light bulb lying on its side"></div>
    <div class="hero-copy">
      <h1 class="hero-title">How to save money<br>with electricity</h1>
      <p class="hero-lead">Review your current home energy usage and save more.</p>
    </div>
    <a class="btn btn-learn">Learn more</a>
  </section>
</header>

<section class="feature" style="left:59px">
  <div class="feature-photo photo-laundry" role="img" aria-label="Photo of a mother and child loading a washing machine"></div>
  <div class="feature-text">
    <p>Lorem ipsum dolor sit amet, consectetur adipisicing elit, sed do eiusmod tempor incididunt ut labore et dolore magna aliqua. Dolor sit amet, consectetur adipisicing elit, sed do eiusmod. Lorem ipsum dolor sit amet, consectetur adipisicing elit, sed do eiusmod tempor incididunt ut labore et dolore magna aliqua. Dolor sit amet, consectetur adipisicing elit, sed do eiusmod.</p>
    <p>Lorem ipsum dolor sit amet, consectetur adipisicing elit, sed do eiusmod tempor incididunt ut labore et dolore magna aliqua. Dolor sit amet, consectetur adipisicing elit, sed do eiusmod. Lorem ipsum dolor sit amet, consectetur adipisicing elit, sed do eiusmod tempor incididunt ut labore et dolore magna aliqua. Dolor sit amet, consectetur adipisicing elit, sed do eiusmod.</p>
  </div>
</section>

<section class="feature" style="left:344px">
  <div class="feature-photo photo-meters" role="img" aria-label="Photo of two analog power meters"></div>
  <div class="feature-text">
    <p>Lorem ipsum dolor sit amet, consectetur adipisicing elit, sed do eiusmod tempor incididunt ut labore et dolore magna aliqua. Dolor sit amet, consectetur adipisicing elit, sed do eiusmod. Lorem ipsum dolor sit amet, consectetur adipisicing elit, sed do eiusmod tempor incididunt ut labore et dolore magna aliqua. Dolor sit amet, consectetur adipisicing elit, sed do eiusmod.</p>
    <p>Lorem ipsum dolor sit amet, consectetur adipisicing elit, sed do eiusmod tempor incididunt ut labore et dolore magna aliqua. Dolor sit amet, consectetur adipisicing elit, sed do eiusmod. Lorem ipsum dolor sit amet, consectetur adipisicing elit, sed do eiusmod tempor incididunt ut labore et dolore magna aliqua. Dolor sit amet, consectetur adipisicing elit, sed do eiusmod.</p>
  </div>
</section>

<section class="feature" style="left:631px">
  <div class="feature-photo photo-bulbs" role="img" aria-label="Photo of two energy saving light bulbs"></div>
  <div class="feature-text">
    <p>Lorem ipsum dolor sit amet, consectetur adipisicing elit, sed do eiusmod tempor incididunt ut labore et dolore magna aliqua. Dolor sit amet, consectetur adipisicing elit, sed do eiusmod. Lorem ipsum dolor sit amet, consectetur adipisicing elit, sed do eiusmod tempor incididunt ut labore et dolore magna aliqua. Dolor sit amet, consectetur adipisicing elit, sed do eiusmod.</p>
    <p>Lorem ipsum dolor sit amet, consectetur adipisicing elit, sed do eiusmod tempor incididunt ut labore et dolore magna aliqua. Dolor sit amet, consectetur adipisicing elit, sed do eiusmod. Lorem ipsum dolor sit amet, consectetur adipisicing elit, sed do eiusmod tempor incididunt ut labore et dolore magna aliqua. Dolor sit amet, consectetur adipisicing elit, sed do eiusmod.</p>
  </div>
</section>

<a class="btn btn-cta" style="left:104px;width:155px">Save energy</a>
<a class="btn btn-cta" style="left:380px;width:180px">Cut high bills</a>
<a class="btn btn-cta" style="left:663px;width:180px">Technology</a>

<footer class="footer">
  <nav class="footer-nav"><a>Home</a><span class="sep">|</span><a>About Us</a><span class="sep">|</span><a>News</a><span class="sep">|</span><a>Contact</a></nav>
  <div class="footer-brand">uns-gefaellt-der-Ruhetag.de</div>
  <div class="footer-copy">Copyright © 2012</div>
</footer>
</body>
</html>
```